21 Day Holiday Challenge

I need 11X17 poster design. I have a generic poster that I've attached but I want a much better design and color scheme to match a holiday challenge but still use our logo. All the details (please include all of the copy/text) are in the poster attached. I also included my Zorvanic Bootcamp logo. I want the poster to look more like a concert poster or big event poster...not a generic homemade poster like the one I provided. I can't wait to see what people come up with!

```html
<!DOCTYPE html>
<html lang="en">
<head>
<meta charset="utf-8">
<title>21 Day Holiday Challenge – Zorvanic Bootcamps</title>
<link href="https://fonts.googleapis.com/css2?family=Oswald:wght@300;400;500;600;700&display=swap" rel="stylesheet">
<style>
  :root {
    --stage: #cfcfcf;
    --blue-deep: #1b4f92;
    --blue-mid: #2f73c4;
    --blue-light: #5b9be0;
    --band-blue: #4a8bd4;
    --orange: #f26a21;
    --orange-light: #ff8a3a;
    --white: #ffffff;
    --black: #050505;
  }
  * { margin: 0; padding: 0; box-sizing: border-box; }
  html, body { width: 1200px; height: 1000px; overflow: hidden; background: var(--stage); }
  body { font-family: "Oswald", "Arial Narrow", sans-serif; color: var(--white); }

  .poster {
    position: absolute; left: 277px; top: 0; width: 646px; height: 1000px; overflow: hidden;
    background: radial-gradient(ellipse 70% 45% at 50% 35%, var(--blue-light) 0%, var(--blue-mid) 45%, var(--blue-deep) 100%);
  }
  .swoosh { position: absolute; left: 0; top: 0; width: 646px; height: 600px; }
  .athletes {
    position: absolute; left: 80px; top: 14px; width: 220px; height: 578px;
    background: linear-gradient(180deg, #c99a7e 0%, #b07a5c 40%, #3a3a3c 62%, #c48e70 80%, #7fd63a 100%);
    border-radius: 90px 90px 40px 40px; opacity: .85;
  }
  .brand-name {
    position: absolute; left: 353px; top: 316px; width: 242px; text-align: center;
    font-weight: 700; font-size: 27px; line-height: 1.1; letter-spacing: 1px; text-transform: uppercase;
  }
  .price-intro { position: absolute; right: 150px; top: 396px; font-weight: 300; font-size: 24px; line-height: 1.2; white-space: nowrap; }
  .price-intro sup, .price-main sup, .price-client sup { font-size: .5em; vertical-align: .8em; line-height: 0; }
  .price-main { position: absolute; right: 51px; top: 418px; font-weight: 600; font-size: 72px; line-height: 1.2; white-space: nowrap; }
  .price-client { position: absolute; right: 56px; top: 512px; font-weight: 300; font-style: italic; font-size: 12px; white-space: nowrap; }

  .headline {
    position: absolute; left: 0; width: 100%; top: 612px; text-align: center; white-space: nowrap;
    font-weight: 600; font-size: 49px; line-height: 1.2;
  }
  .subhead {
    position: absolute; left: 0; width: 100%; top: 678px; text-align: center; white-space: nowrap;
    font-weight: 400; font-size: 22px; line-height: 1.2; text-transform: uppercase;
  }
  .subhead .hot { color: var(--orange); font-weight: 600; }
  .teaser { position: absolute; left: 0; width: 100%; top: 749px; text-align: center; white-space: nowrap; font-size: 10.5px; font-weight: 300; }
  .teaser strong { font-weight: 600; }

  .deadline-band {
    position: absolute; left: 0; top: 778px; width: 100%; height: 68px; background: var(--band-blue); text-align: center;
  }
  .deadline { padding-top: 5px; font-size: 13.5px; font-weight: 300; white-space: nowrap; line-height: 1.3; }
  .deadline strong { font-weight: 600; }
  .offer-start { font-size: 24px; font-weight: 600; line-height: 1.5; white-space: nowrap; }

  .benefits-band { position: absolute; left: 0; top: 846px; width: 100%; height: 154px; background: var(--black); }
  .benefits { display: flex; padding: 12px 0 0 20px; }
  .benefit {
    padding: 0 22px; text-align: center; font-size: 11.5px; line-height: 1.38; font-weight: 400;
    border-left: 1px solid var(--white);
  }
  .benefit:nth-child(1) { width: 154px; border-left: none; padding: 0 18px; }
  .benefit:nth-child(2) { width: 164px; }
  .benefit:nth-child(3) { width: 136px; }
  .benefit:nth-child(4) { width: 138px; padding: 0 16px; }
  .site { position: absolute; left: 0; width: 100%; top: 84px; text-align: center; color: var(--orange); font-size: 23px; font-weight: 600; }
</style>
</head>
<body>
<main class="poster">
  <svg class="swoosh" viewBox="0 0 646 600" aria-hidden="true">
    <path d="M0 300 C120 340 180 380 260 300 S430 60 646 40 L646 80 C460 95 380 260 270 350 S80 360 0 340 Z" fill="var(--orange)"/>
    <path d="M0 318 C110 360 200 400 275 320 S450 120 646 115 L646 155 C470 160 390 300 290 380 S90 375 0 358 Z" fill="var(--orange-light)"/>
    <ellipse cx="200" cy="580" rx="230" ry="20" fill="#123f7a" opacity=".35"/>
  </svg>

  <div class="athletes" role="img" aria-label="Photo of a fit man and woman standing back to back holding dumbbells"></div>

  <div class="brand-name">Zorvanic Bootcamps</div>

  <p class="price-intro">A <sup>$</sup>299 value for</p>
  <p class="price-main">ONLY <sup>$</sup>69</p>
  <p class="price-client">(Clients <sup>$</sup>39)</p>

  <h1 class="headline">21 DAY HOLIDAY CHALLENGE</h1>
  <p class="subhead">Discover the secret to <span class="hot">losing weight</span> this holiday season<br>in just 21 days with this <span class="hot">amazing new program!</span></p>
  <p class="teaser">Imagine… A training and nutrition program so effective, you could get 3x the fat loss in <strong>IN JUST 21 DAYS - DURING THE HOLIDAYS!!!</strong></p>

  <section class="deadline-band">
    <p class="deadline">HURRY! Registration closes Thursday, October 30th!!!&nbsp; CLAIM YOUR SPOT NOW, <strong>CALL (555) 014-2287</strong></p>
    <h2 class="offer-start">HERE’S WHAT YOU GET STARTING NOVEMBER 3RD, 2014</h2>
  </section>

  <section class="benefits-band">
    <div class="benefits">
      <p class="benefit">Training sessions designed to incinerate fat off your midsection, thighs, and arms</p>
      <p class="benefit">Fat-melting nutrition guides, stress management tips, delicious recipes and BONUS workouts</p>
      <p class="benefit">A success session to map out your individual plan for success</p>
      <p class="benefit">Access to our Zorvanic VIP Accountability page to ensure you get results</p>
    </div>
    <p class="site">ZorvanicFit.com</p>
  </section>
</main>
</body>
</html>
```